Business card design for IT consulting company

Looking for a simple, modern, clean business card design.
Open to reworking our existing logo.

Attached is our current business cards which we do not like.
Ideally double sided with something simple on the back.
Rectangle / Horizonal only.
No rounded edges on the card.
White as the dominate color is preferred.

Target Market(s)

clients, legal, oil & gas, medical, professionals

Industry/Entity Type

IT, tech, consulting

Contact Information for Business Card

Name, Title, email, phone, cell, website

Font styles to use
Sans Serif

Requirements
Must have
• Clean design
Should not have
• loud colors or unusual fonts, etc

```html
<!DOCTYPE html>
<html lang="en">
<head>
<meta charset="utf-8">
<title>Norvex Solutions – Business Card</title>
<link rel="stylesheet" href="https://fonts.googleapis.com/css2?family=Poppins:wght@700&family=Open+Sans:wght@300;700;800&display=swap">
<style>
  :root {
    --backdrop: #ededed;
    --card-white: #ffffff;
    --ink-dark: #1f2730;
    --slate: #2b333d;
    --accent-red: #e2404f;
    --accent-yellow: #f1bb2b;
    --title-blue: #2b4ea3;
    --card-w: 560px;
    --card-h: 320px;
  }
  * { box-sizing: border-box; margin: 0; padding: 0; }
  html, body {
    width: 1200px;
    height: 900px;
    overflow: hidden;
    background: var(--backdrop);
  }
  .canvas {
    position: relative;
    width: 1200px;
    height: 900px;
  }
  .card {
    position: absolute;
    left: 320px;
    width: var(--card-w);
    height: var(--card-h);
    background: var(--card-white);
    box-shadow: 0 6px 18px rgba(0, 0, 0, 0.12);
    overflow: hidden;
  }
  .card--front { top: 110px; }
  .card--back { top: 470px; }

  /* Front: slim colour bands framing the wordmark */
  .edge-bands {
    position: absolute;
    top: 0;
    bottom: 0;
    display: flex;
  }
  .edge-bands--left { left: 0; }
  .edge-bands--right { right: 0; flex-direction: row-reverse; }
  .band { height: 100%; }
  .band--dark { width: 22px; background: var(--slate); }
  .band--red { width: 6px; background: var(--accent-red); }
  .band--yellow { width: 6px; background: var(--accent-yellow); }

  .brand {
    position: absolute;
    left: 0;
    right: 0;
    top: 140px;
    display: flex;
    justify-content: center;
    align-items: center;
    gap: 12px;
  }
  .brand__square {
    width: 40px;
    height: 40px;
    background: var(--accent-red);
  }
  .brand__name {
    font-family: "Poppins", sans-serif;
    font-weight: 700;
    font-size: 38px;
    line-height: 1;
    color: var(--ink-dark);
    letter-spacing: -0.5px;
  }

  /* Back: plain dark panel with two accent stripes */
  .back-panel {
    position: absolute;
    left: 0;
    top: 0;
    bottom: 0;
    width: 236px;
    background: var(--slate);
    display: flex;
    align-items: center;
    justify-content: center;
  }
  .back-panel__stripes {
    position: absolute;
    right: -14px;
    top: 0;
    bottom: 0;
    display: flex;
  }
  .back-brand {
    font-family: "Poppins", sans-serif;
    font-weight: 700;
    font-size: 30px;
    color: #ffffff;
  }

  .contact {
    position: absolute;
    left: 290px;
    top: 44px;
    font-family: "Open Sans", sans-serif;
    color: var(--ink-dark);
  }
  .contact__name {
    font-weight: 800;
    font-size: 26px;
    line-height: 1.1;
  }
  .contact__title {
    font-weight: 300;
    font-size: 24px;
    line-height: 1.2;
    color: var(--title-blue);
    padding-bottom: 4px;
    border-bottom: 2px solid var(--accent-red);
    display: inline-block;
    margin-bottom: 14px;
  }
  .contact__list { list-style: none; }
  .contact__item {
    display: flex;
    align-items: center;
    gap: 8px;
    font-weight: 700;
    font-size: 13px;
    height: 30px;
  }
  .contact__icon { width: 22px; height: 22px; flex: none; }
  .icon-disc { fill: var(--ink-dark); }
  .icon-disc--red { fill: var(--accent-red); }
  .icon-line { fill: none; stroke: #ffffff; stroke-width: 1.4; }
  .icon-fill { fill: #ffffff; }
</style>
</head>
<body>
<main class="canvas">

  <section class="card card--front" aria-label="Business card front">
    <div class="edge-bands edge-bands--left" aria-hidden="true">
      <span class="band band--dark"></span>
      <span class="band band--red"></span>
    </div>
    <div class="edge-bands edge-bands--right" aria-hidden="true">
      <span class="band band--dark"></span>
      <span class="band band--yellow"></span>
    </div>
    <div class="brand">
      <span class="brand__square"></span>
      <span class="brand__name">Norvex Solutions</span>
    </div>
  </section>

  <section class="card card--back" aria-label="Business card back">
    <div class="back-panel">
      <span class="back-brand">Norvex</span>
      <div class="back-panel__stripes" aria-hidden="true">
        <span class="band band--red"></span>
        <span class="band band--yellow"></span>
      </div>
    </div>

    <div class="contact">
      <p class="contact__name">Daniel Reyes</p>
      <p class="contact__title">IT Consultant</p>
      <ul class="contact__list">
        <li class="contact__item">
          <svg class="contact__icon" viewBox="0 0 22 22" aria-hidden="true">
            <circle class="icon-disc" cx="11" cy="11" r="11"/>
            <rect class="icon-line" x="5" y="7" width="12" height="8"/>
            <polyline class="icon-line" points="5,7 11,12 17,7"/>
          </svg>
          daniel.reyes@norvex.ca
        </li>
        <li class="contact__item">
          <svg class="contact__icon" viewBox="0 0 22 22" aria-hidden="true">
            <circle class="icon-disc" cx="11" cy="11" r="11"/>
            <path class="icon-fill" d="M7 5.5l2.2-.5 1.3 3-1.4 1.1a7 7 0 0 0 3.3 3.3l1.1-1.4 3 1.3-.5 2.2c-4.8.4-9.4-4.2-9-9z"/>
          </svg>
          (888) 555-0142
        </li>
        <li class="contact__item">
          <svg class="contact__icon" viewBox="0 0 22 22" aria-hidden="true">
            <circle class="icon-disc" cx="11" cy="11" r="11"/>
            <rect class="icon-line" x="7.5" y="4.5" width="7" height="13" rx="1"/>
            <circle class="icon-fill" cx="11" cy="15.5" r="0.8"/>
          </svg>
          (604) 555-0187
        </li>
        <li class="contact__item">
          <svg class="contact__icon" viewBox="0 0 22 22" aria-hidden="true">
            <circle class="icon-disc icon-disc--red" cx="11" cy="11" r="11"/>
            <circle class="icon-line" cx="11" cy="11" r="6"/>
            <ellipse class="icon-line" cx="11" cy="11" rx="2.6" ry="6"/>
            <line class="icon-line" x1="5" y1="11" x2="17" y2="11"/>
          </svg>
          www.norvex.ca
        </li>
      </ul>
    </div>
  </section>

</main>
</body>
</html>
```